Vertical Banner

I need an eye-catching banner created for street fairs, indoor and outdoor events to draw attention to our language school. It will be to print on this banner (specs included):
https://www.printvalemart.com/tag/317/Retractable-Banners/product/5146-71/Basic-Rollup-Banner-Stand-29-14

I want the banner to be:
- SIMPLE
- Eye catching (not busy with too many pictures or information)
- It should say at top prominently: "Come learn a language!" and have our name.
- Below these languages should be large and eye-catching: Spanish, Chinese, French, Russian, German, Italian, Farsi, Turkish, Portuguese, ASL, Cantonese, Japanese, Korean, Vietnamese, Arabic, Dutch, more... (if some need to be cut our because of overcrowding let me know OR we can make some big and others small)
- Below this it should have GROUP & PRIVATE LESSONS
- It should be colorful and make people think of things international - perhaps national flags in background? Or images of world famous monuments? Could be image of adutls in a classroom. Sth that gets people excited about travel and language learning
- It should have our contact info VERY large at bottom:
Zephyr Languages -
San Francisco, Silicon Valley & New York City
www.zephyrlanguagesf.com
415-926-1548
info@zephyrlanguagesf.com
(this can be smaller)
Two Halvorsen Plaza
Lobby 4
San Francisco, CA 94108

Hey Designers, please feel free to do a rough take on it. I don't need you to spend too much time, just give me a general idea of how you would make it look, then i know we can go from there later and refine it. Feel free to make it more of a quick sketch to show how you would do it.

Target Market(s)

adults from about 25-55 years old, educated, employed and typically world travellers

Industry/Entity Type

School

Colors
86cfc6
00a990
cadf82
acd036
9bcb3c
fbed22
f78f20
ffc214
f37122

Requirements
Must have
• Must be simple! Too many banners put way too much information and pictures. I want someone to walk by and immediately know we teach foreign languages. Must have bright colors and large font for languages offered
Should not have
• Should not be too full of images and design that distract the viewer from seeing the main thing I want them to see: that we teacher languages

```html
<!DOCTYPE html>
<html lang="en">
<head>
<meta charset="utf-8">
<title>Zephyr Languages – Rollup Banner</title>
<link rel="stylesheet" href="https://fonts.googleapis.com/css2?family=Open+Sans:ital,wght@0,400;0,600;0,700;0,800;1,800&family=PT+Sans+Narrow:wght@400;700&display=swap">
<style>
  :root {
    --stage: #e4e4e4;
    --paper: #ffffff;
    --sky-light: #e6f5f4;
    --sky: #9fd8d6;
    --teal-text: #3d8590;
    --ink: #0d3b47;
    --ink-dark: #0b1a20;
    --band: #023a48;
    --ring: #4f8d99;
    --ring-light: #7fb4bd;
    --globe: #eaf6f6;
    --globe-edge: #5aa89a;
    --accent-red: #e52420;
    --l1: #e8206e;
    --l2: #e8206e;
    --l3: #b9348f;
    --l4: #acd036;
    --l5: #3f4fa0;
    --l6: #8d47a0;
    --l7: #f37122;
    --l8: #5d9c3a;
    --white: #ffffff;
  }
  * { box-sizing: border-box; margin: 0; padding: 0; }
  html, body { width: 1200px; height: 1200px; overflow: hidden; background: var(--stage); }

  .banner {
    position: absolute;
    left: 381px; top: 24px;
    width: 498px; height: 1308px;
    transform: scale(0.88);
    transform-origin: top left;
    background: linear-gradient(to bottom, var(--paper) 0, var(--paper) 330px, var(--sky-light) 430px, var(--sky) 520px, var(--sky) 100%);
    overflow: hidden;
    font-family: "Open Sans", sans-serif;
    text-align: center;
  }
  .headline { position: absolute; left: 0; right: 0; }
  .headline-come {
    top: 30px; font-size: 52px; font-weight: 400; letter-spacing: 30px; padding-left: 30px;
    color: var(--teal-text); line-height: 1;
  }
  .headline-learn {
    top: 88px; font-size: 74px; font-weight: 700; color: var(--ink); line-height: 1; letter-spacing: -1px;
  }
  .headline-language {
    top: 164px; font-size: 74px; font-weight: 700; line-height: 1; letter-spacing: -1px; padding-left: 14px;
  }
  .headline-language span:nth-child(1) { color: var(--l1); }
  .headline-language span:nth-child(2) { color: var(--l2); }
  .headline-language span:nth-child(3) { color: var(--l3); }
  .headline-language span:nth-child(4) { color: var(--l4); }
  .headline-language span:nth-child(5) { color: var(--l5); }
  .headline-language span:nth-child(6) { color: var(--l6); }
  .headline-language span:nth-child(7) { color: var(--l7); }
  .headline-language span:nth-child(8) { color: var(--l8); }

  .brand-name {
    position: absolute; left: 0; right: 0; top: 268px;
    color: var(--ink-dark); font-weight: 800; line-height: 1.02;
  }
  .brand-name .brand-top { display: block; font-size: 92px; letter-spacing: -1px; }
  .brand-name .brand-bottom { display: block; font-size: 58px; padding-left: 14px; }

  .world-ring { position: absolute; left: 0; top: 440px; width: 498px; height: 600px; }

  .language-cloud {
    position: absolute; left: 54px; top: 562px; width: 378px;
    display: flex; flex-direction: column; align-items: center;
    color: var(--ink-dark); line-height: 1;
  }
  .language-cloud .row { display: flex; align-items: baseline; gap: 8px; white-space: nowrap; }
  .lang-heavy { font-weight: 800; }
  .lang-bold { font-weight: 700; }
  .lang-light { font-weight: 400; }
  .lang-narrow { font-family: "PT Sans Narrow", sans-serif; font-weight: 400; }
  .lang-narrow-bold { font-family: "PT Sans Narrow", sans-serif; font-weight: 700; }
  .lang-more { color: var(--accent-red); font-weight: 800; font-style: italic; font-size: 22px; margin-top: 4px; }

  .lesson-art { position: absolute; }
  .lesson-art--group { left: 41px; top: 945px; }
  .lesson-art--private { left: 356px; top: 947px; }

  .lessons-label {
    position: absolute; left: 0; right: 0; top: 992px;
    font-family: "PT Sans Narrow", sans-serif; font-weight: 700; font-size: 31px;
    color: var(--ink-dark); line-height: 41px; padding-left: 14px;
  }

  .contact-band { position: absolute; left: 0; top: 1075px; width: 498px; height: 233px; }
  .contact {
    position: absolute; left: 0; right: 0; top: 1122px;
    font-family: "PT Sans Narrow", sans-serif; font-weight: 700; color: var(--white); line-height: 1;
    padding-left: 6px;
  }
  .contact-name { font-size: 42px; }
  .contact-cities { font-size: 23px; margin-top: 8px; }
  .contact-lines { font-size: 26px; margin-top: 13px; }
  .contact-web { font-size: 41px; margin-top: 6px; }
</style>
</head>
<body>
  <main class="banner">
    <div class="headline headline-come">COME</div>
    <div class="headline headline-learn">LEARN A</div>
    <div class="headline headline-language" aria-label="LANGUAGE"><span>L</span><span>A</span><span>N</span><span>G</span><span>U</span><span>A</span><span>G</span><span>E</span></div>

    <h1 class="brand-name"><span class="brand-top">Zephyr</span><span class="brand-bottom">LANGUAGES</span></h1>

    <svg class="world-ring" viewBox="0 0 498 600" role="img" aria-label="Ring of world landmarks, hot-air balloons and planes around a globe">
      <defs>
        <radialGradient id="ring-fill" cx="50%" cy="50%" r="50%">
          <stop offset="70%" stop-color="var(--ring)"/>
          <stop offset="100%" stop-color="var(--ring-light)"/>
        </radialGradient>
      </defs>
      <circle cx="244" cy="295" r="238" fill="url(#ring-fill)" opacity="0.85"/>
      <circle cx="242" cy="295" r="190" fill="var(--globe)" stroke="var(--globe-edge)" stroke-width="4"/>
    </svg>

    <div class="language-cloud">
      <div class="row"><span class="lang-heavy" style="font-size:40px">FRENCH</span></div>
      <div class="row"><span class="lang-bold" style="font-size:34px">CHINESE</span><span class="lang-light" style="font-size:25px">TURKISH</span></div>
      <div class="row"><span class="lang-bold" style="font-size:33px">SPANISH</span><span class="lang-narrow" style="font-size:45px">GERMAN</span></div>
      <div class="row"><span class="lang-narrow" style="font-size:50px">ITALIAN</span><span class="lang-bold" style="font-size:32px">FARSI</span></div>
      <div class="row"><span class="lang-bold" style="font-size:32px">ASL</span><span class="lang-heavy" style="font-size:40px">RUSSIAN</span></div>
      <div class="row"><span class="lang-light" style="font-size:23px;letter-spacing:8px">PORTUGUESE</span></div>
      <div class="row"><span class="lang-narrow-bold" style="font-size:46px">JAPANESE</span><span class="lang-bold" style="font-size:22px">CANTONESE</span></div>
      <div class="row"><span class="lang-bold" style="font-size:31px">KOREAN</span><span class="lang-light" style="font-size:31px">ARABIC</span></div>
      <div class="row"><span class="lang-narrow" style="font-size:26px">VIETNAMESE</span><span class="lang-narrow" style="font-size:36px">DUTCH</span></div>
      <div class="row"><span class="lang-more">MORE.....</span></div>
    </div>

    <svg class="lesson-art lesson-art--group" width="108" height="108" viewBox="0 0 108 108" role="img" aria-label="Group class with a teacher at a board">
      <circle cx="54" cy="54" r="53" fill="#eef8f6"/>
      <circle cx="54" cy="54" r="36" fill="#7aa8b4" opacity="0.45"/>
    </svg>
    <svg class="lesson-art lesson-art--private" width="108" height="108" viewBox="0 0 108 108" role="img" aria-label="Private lesson with tutor and student at a desk">
      <circle cx="54" cy="54" r="53" fill="#ffffff"/>
      <circle cx="54" cy="54" r="36" fill="#5c9fc2" opacity="0.4"/>
    </svg>

    <div class="lessons-label">GROUP &amp;<br>PRIVATE LESSONS</div>

    <svg class="contact-band" viewBox="0 0 498 233" preserveAspectRatio="none" aria-hidden="true">
      <path d="M0 30 Q249 -10 498 30 L498 233 L0 233 Z" fill="var(--band)"/>
    </svg>
    <div class="contact">
      <div class="contact-name">Zephyr Languages</div>
      <div class="contact-cities">San Francisco, Silicon Valley &amp; New York City</div>
      <div class="contact-lines">415-926-1548 &nbsp;|&nbsp; info@zephyrlanguagesf.com</div>
      <div class="contact-web">www.zephyrlanguagesf.com</div>
    </div>
  </main>
</body>
</html>
```